Dance Card to Provide Contact Info

I'm looking for a double sided business card to provide contact information to perspective dance partners.
One side of the card would have the words: "Yes I would love to Dance" written in an interesting and eye catching way. Below that would be the three categories I'm interested in
>Social >Exhibition >Competition
The other side of the card would include a picture of me with my Name, Phone Number, and Email Address (Dale Penwick, 210-547-2183, dale@twirlmerry.dance)
My target market is middle aged women interested in Country and Western dancing and West Coast Swing dancing. I am NOT particularly interested in Ballroom style.
Here are a few links to the type of dancing I want to do:
http://www.fpqlx.org/
http://www.prairiestepguildnetwork.com/
http://bexarridgepartnerspin.com/
Business
Contact Information for Business Card
Dale Penwick
210-547-2183
dale@twirlmerry.dance

```html
<!DOCTYPE html>
<html lang="en">
<head>
<meta charset="utf-8">
<title>TwirlMerry Dance – Business Card</title>
<link href="https://fonts.googleapis.com/css2?family=Roboto:wght@300;400;700&display=swap" rel="stylesheet">
<style>
  :root {
    --canvas-bg: #ece9e4;
    --card-red: #a32a24;
    --card-red-dark: #7e1c18;
    --card-red-light: #b8352c;
    --paper-light: #ffffff;
    --paper-grey: #d9d9d9;
    --ink: #1c1c1c;
    --ink-soft: #444444;
    --white: #ffffff;
  }
  * { margin: 0; padding: 0; box-sizing: border-box; }
  html, body {
    width: 1200px;
    height: 1023px;
    overflow: hidden;
    background: var(--canvas-bg);
    font-family: "Roboto", Arial, sans-serif;
  }
  .canvas {
    position: relative;
    width: 1200px;
    height: 1023px;
  }
  .card {
    position: absolute;
    left: 220px;
    width: 760px;
    height: 434px;
    border-radius: 22px;
    overflow: hidden;
    box-shadow: 0 6px 18px rgba(0,0,0,0.18);
  }

  /* ---------- Front side ---------- */
  .card--front {
    top: 58px;
    background: radial-gradient(ellipse at 40% 45%, var(--paper-light) 0%, #f1f1f1 45%, var(--paper-grey) 100%);
  }
  .brand {
    position: absolute;
    display: flex;
    align-items: center;
    gap: 16px;
  }
  .brand__mark {
    width: 64px;
    height: 64px;
    border-radius: 50%;
    background: var(--ink);
    flex: none;
  }
  .brand__name {
    font-weight: 700;
    font-size: 40px;
    letter-spacing: 1px;
    line-height: 1;
  }
  .card--front .brand { left: 46px; top: 80px; }
  .card--front .brand__name { color: var(--card-red); }

  .holder-name {
    position: absolute;
    left: 46px;
    top: 238px;
    font-size: 34px;
    font-weight: 400;
    color: var(--ink);
  }
  .divider {
    position: absolute;
    left: 0;
    top: 292px;
    width: 478px;
    height: 3px;
    background: var(--card-red);
  }
  .contact {
    position: absolute;
    left: 46px;
    top: 318px;
    list-style: none;
  }
  .contact__item {
    display: flex;
    align-items: center;
    gap: 12px;
    font-size: 20px;
    font-weight: 400;
    color: var(--ink-soft);
    letter-spacing: 0.5px;
    margin-bottom: 14px;
  }
  .contact__icon { width: 18px; height: 18px; flex: none; }
  .portrait {
    position: absolute;
    right: 0;
    top: 0;
    width: 290px;
    height: 100%;
    background: linear-gradient(180deg, #f4f4f4 0%, #e5d2c4 30%, #2a2a2a 55%, #151515 100%);
  }

  /* ---------- Back side ---------- */
  .card--back {
    top: 532px;
    background: linear-gradient(160deg, var(--card-red-light) 0%, var(--card-red) 50%, var(--card-red-dark) 100%);
  }
  .card--back .brand {
    left: 50%;
    top: 62px;
    transform: translateX(-50%);
  }
  .card--back .brand__name { color: var(--white); font-size: 46px; }
  .tagline {
    position: absolute;
    left: 0;
    right: 0;
    top: 212px;
    display: flex;
    align-items: center;
    gap: 18px;
    color: var(--white);
    font-size: 26px;
    font-weight: 300;
    letter-spacing: 1.5px;
    white-space: nowrap;
  }
  .tagline::before,
  .tagline::after {
    content: "";
    flex: 1;
    height: 2px;
    background: var(--white);
  }
  .tagline::before { flex: 0 0 150px; }
  .categories {
    position: absolute;
    left: 60px;
    right: 60px;
    top: 284px;
    display: flex;
    justify-content: space-between;
    list-style: none;
    color: var(--white);
    font-size: 22px;
    font-weight: 400;
    letter-spacing: 1px;
  }
  .categories li::before { content: "\2022"; }
  .white-band {
    position: absolute;
    left: 0;
    right: 0;
    top: 340px;
    height: 48px;
    background: linear-gradient(180deg, #ffffff 0%, #e6e6e6 100%);
  }
</style>
</head>
<body>
<main class="canvas">

  <section class="card card--front" aria-label="Business card front">
    <div class="brand">
      <span class="brand__mark"></span>
      <span class="brand__name">TwirlMerry Dance</span>
    </div>
    <h1 class="holder-name">Dale Penwick</h1>
    <div class="divider"></div>
    <ul class="contact">
      <li class="contact__item">
        <svg class="contact__icon" viewBox="0 0 24 24" aria-hidden="true">
          <circle cx="12" cy="12" r="10.5" fill="none" stroke="#a32a24" stroke-width="2"/>
          <path d="M9 7.5c-1 .6-1.4 1.6-.9 3 .8 2.2 2.4 3.9 4.5 4.8 1.3.5 2.3.2 3-.8l-1.6-1.5-1.3.7c-1-.5-1.8-1.3-2.3-2.3l.7-1.3z" fill="#a32a24"/>
        </svg>
        210-547-2183
      </li>
      <li class="contact__item">
        <svg class="contact__icon" viewBox="0 0 24 24" aria-hidden="true">
          <rect x="2" y="5" width="20" height="14" fill="none" stroke="#a32a24" stroke-width="2"/>
          <path d="M2 5l10 8 10-8" fill="none" stroke="#a32a24" stroke-width="2"/>
        </svg>
        dale@twirlmerry.dance
      </li>
    </ul>
    <div class="portrait" role="img" aria-label="Portrait photo of Dale Penwick, smiling, in a black shirt"></div>
  </section>

  <section class="card card--back" aria-label="Business card back">
    <div class="brand">
      <span class="brand__mark"></span>
      <span class="brand__name">TwirlMerry Dance</span>
    </div>
    <p class="tagline">Yes I would love to Dance</p>
    <ul class="categories">
      <li>Social</li>
      <li>Exhibition</li>
      <li>Competition</li>
    </ul>
    <div class="white-band"></div>
  </section>

</main>
</body>
</html>
```